Bluebird Business Card Design

Name Marlene Obadofor
Title Mortgage Originator
Office (800) 416-2795 x65
Direct (240) 615-2079
Email mobadofor@bluebirdlending.example
NMLS 3817465
Licensed MD

Name Dorian Pelletier
Title Mortgage Originator
Office (800) 416-2795 x66
Direct (404) 263-5147
Email dpelletier@bluebirdlending.example
NMLS 3156702
Licensed MD

Name Rochelle Barnaby
Title Mortgage Originator
Office (800) 416-2795 x67
Direct (443) 812-3659
Email barnabyrochelle@mailpost.example
NMLS 3902576
Licensed MD

Name Omar Teldouri
Title Mortgage Originator
Office (800) 416-2795 x32
Direct (571) 326-7045
Email oteldouri@bluebirdlending.example
NMLS 1573064
Licensed MD

```html
<!DOCTYPE html>
<html lang="en">
<head>
<meta charset="utf-8">
<title>Rochelle Barnaby – Business Card</title>
<link rel="stylesheet" href="https://fonts.googleapis.com/css2?family=Montserrat:wght@400;500;700&display=swap">
<style>
  :root {
    --page-bg: #e9e4de;
    --card-bg: #efe9e2;
    --card-edge: #f8f4ef;
    --ink-strong: #1d1b1a;
    --ink: #3a3633;
    --photo-light: #e6c4a4;
    --photo-mid: #c9956c;
    --photo-dark: #7a5036;
  }
  * { box-sizing: border-box; margin: 0; padding: 0; }
  html, body {
    width: 1200px;
    height: 1047px;
    overflow: hidden;
    background: var(--page-bg);
    font-family: "Montserrat", sans-serif;
  }
  .card {
    position: absolute;
    left: 100px;
    top: 250px;
    width: 1000px;
    height: 546px;
    background: var(--card-bg);
    border: 2px solid var(--card-edge);
    border-radius: 30px;
    overflow: hidden;
    box-shadow: 0 10px 40px rgba(90, 70, 50, 0.12);
  }
  .identity {
    position: absolute;
    left: 48px;
    top: 84px;
  }
  .name {
    font-weight: 700;
    font-size: 41px;
    letter-spacing: 1px;
    color: var(--ink-strong);
    text-transform: uppercase;
    line-height: 1;
  }
  .title {
    margin-top: 14px;
    font-size: 22px;
    font-weight: 500;
    color: var(--ink);
  }
  .contacts {
    position: absolute;
    left: 48px;
    top: 228px;
    list-style: none;
  }
  .contacts li {
    display: flex;
    align-items: center;
    gap: 10px;
    font-size: 22px;
    color: var(--ink);
    height: 38px;
  }
  .contacts svg { width: 22px; height: 22px; fill: var(--ink-strong); flex: none; }
  .license {
    position: absolute;
    left: 44px;
    top: 392px;
    font-size: 22px;
    font-weight: 500;
    color: var(--ink);
    line-height: 38px;
  }
  .portrait {
    position: absolute;
    left: 638px;
    top: 36px;
    width: 330px;
    height: 510px;
    border-radius: 160px 160px 0 0;
    background: linear-gradient(180deg, var(--photo-mid) 0%, var(--photo-light) 45%, var(--photo-mid) 80%, var(--photo-dark) 100%);
  }
</style>
</head>
<body>
  <section class="card">
    <div class="identity">
      <h1 class="name">Rochelle Barnaby</h1>
      <p class="title">Mortgage Originator</p>
    </div>

    <ul class="contacts">
      <li>
        <svg viewBox="0 0 24 24" aria-hidden="true"><path d="M3 9c0-3 4-5 9-5s9 2 9 5v1.5c0 .8-.7 1.3-1.4 1.1l-3-.9c-.6-.2-1-.7-1-1.3V8.2c-2.4-.6-4.8-.6-7.2 0v1.2c0 .6-.4 1.1-1 1.3l-3 .9C3.7 11.8 3 11.3 3 10.5zM6 13h12l2 6H4z"/></svg>
        <span>(800) 416-2795 x67</span>
      </li>
      <li>
        <svg viewBox="0 0 24 24" aria-hidden="true"><path d="M22 2 2 10.5l7 2.8L19 5l-8 9.5V22l3.8-5 4.2 2z"/></svg>
        <span>(443) 812-3659</span>
      </li>
      <li>
        <svg viewBox="0 0 24 24" aria-hidden="true"><path d="M2 5h20v2l-10 6L2 7zM2 9.3l10 6 10-6V19H2z"/></svg>
        <span>barnabyrochelle@mailpost.example</span>
      </li>
    </ul>

    <div class="license">
      <p>NMLS 3902576</p>
      <p>Licensed MD</p>
    </div>

    <div class="portrait" role="img" aria-label="Portrait photo of Rochelle Barnaby in a satin blouse"></div>
  </section>
</body>
</html>
```